Zielgruppe
Ich bin ein Einzelunternehmen, das Coaching & Seminare anbietet. Alle Infos zu meinem Unternehmen sind auf der Homepage zu finden
www.TormaVita.de
Schwerpunkte meiner Arbeit zu Coaching & Seminaren:
• Hochsensibilität – Feinfühligkeit nutzen, Herausforderungen meistern
• Entspannung – Stress bewältigen, Resilienz trainieren
• Intervision – Kollegial beraten, Teamgeist stärken
• Live-Work-Management – Ressourcen entdecken, Ziele erreichen
Meine Zielgruppen für die obigen Schwerpunkte sind:
Feinfühlige Menschen mit einer hohen Sensibilität
Eltern hochsensibler Kinder
Unternehmen
Aufgabenstellung
Da die Darstellung beim Briefing etwas unübersichtlich geworden ist durch meine Veränderungen, hier nochmals die Übersicht:
Aufgabenstellung:
Ich möchte gerne einen Wickelfalzflyer, 6 Seiten, herzlichen Dank vorab für schöne Designvorschläge :)
Flyer im Design in Farben und Stil passend zur Homepage gestalten, Fotos und Logo einbinden
Schriftart Poppins (Achtung, es gibt zwei Schriftarte Poppins, bitte die verwenden, die auf Homepage ist)
Folgende Kernpunkte mit zu meiner Homepage passenden Texten können in den Flyer eingebaut werden:
- Schwerpunkte meiner Arbeit
- Coaching & Seminare
- Meine Haltung und Arbeitsweise mit meinen drei Schlagworten und meinem Zitat :
• informativ. feinfühlig. lösungsorientiert.
• „Ich begleite mit Feingefühl und tiefer Wertschätzung für das Potential, das in jedem Menschen steckt“
- Qualifikationen
• Lehrerin für Sonderpädagogik
• Systemischer Coach
• Heilpraktikerin für Psychotherapie
• Fachberaterin Hochsensibilität
• Hypnose- und Atem-Coach
• Trainerin für Entspannung, Resilienz, Achtsamkeit, Stressmanagement, Schlafförderung
• Trainerin für das Kallwitzer Balance Ansatz (KBA®)
• u.a.
- Beim Coaching kann der folgende Text eingebaut werden:
Als Coach begleite ich Sie wertschätzend dabei, Ihre Wünsche zu realisieren, Ihre Ziele zu erreichen und Probleme zu lösen.
Orientiert an Ihrem Anliegen entwickeln wir gemeinsam Wege, Ihre Ressourcen zu entdecken, Ihre Resilienz (psychische Widerstandskraft) zu stärken und Ihre sozialen Fähigkeiten (Skills)auszuschöpfen.
F..

```html
<!DOCTYPE html>
<html lang="de">
<head>
<meta charset="utf-8">
<title>Flyer Innenseite – Coaching &amp; Seminare</title>
<link href="https://fonts.googleapis.com/css2?family=Poppins:wght@400&display=swap" rel="stylesheet">
<style>
  :root {
    --paper: #f1f6fc;
    --ink: #1f2a33;
    --accent-line: #7199c3;
    --photo-warm: #d9c4a8;
    --photo-light: #eef0ee;
    --photo-navy: #2c3a4f;
    --leaf: #2f4256;
  }
  * { margin: 0; padding: 0; box-sizing: border-box; }
  html, body { width: 1200px; height: 808px; overflow: hidden; background: var(--paper); }
  .flyer-inner {
    position: relative; width: 1200px; height: 808px; background: var(--paper);
    font-family: "Poppins", sans-serif; font-size: 14px; line-height: 20px; color: var(--ink);
  }
  .fold-curve { position: absolute; left: 0; top: 0; }
  .block { position: absolute; }
  .block p + p { margin-top: 19px; }
  .bullets { list-style: none; }
  .bullets li { position: relative; padding-left: 24px; margin-top: 1.5px; }
  .bullets li::before { content: "•"; position: absolute; left: 2px; }
  .photo { position: absolute; border-radius: 0; }
  .photo--seminar-left {
    left: 67px; top: 230px; width: 276px; height: 225px;
    background: linear-gradient(90deg, var(--photo-light) 0%, #f6f4f0 45%, var(--photo-warm) 100%);
  }
  .photo--coaching {
    left: 431px; top: 58px; width: 338px; height: 225px;
    background: linear-gradient(90deg, #a9c0dc 0%, var(--photo-warm) 35%, #efece6 70%, #d8c2a4 100%);
  }
  .photo--seminar-right {
    left: 853px; top: 339px; width: 282px; height: 225px;
    background: linear-gradient(90deg, #eceeec 0%, #f5f3ef 50%, #c9a98a 80%, #9fb8d4 100%);
  }
  .leaf-mark {
    position: absolute; left: 564px; top: 704px; width: 72px; height: 44px;
    background: var(--leaf); border-radius: 50% 50% 40% 40%; opacity: .85;
  }
</style>
</head>
<body>
<main class="flyer-inner">
  <svg class="fold-curve" width="60" height="808" viewBox="0 0 60 808" aria-hidden="true">
    <path d="M22 0 C 52 220, 50 420, 40 560 C 34 660, 40 740, 47 808" fill="none" stroke="var(--accent-line)" stroke-width="2.5"/>
  </svg>

  <section class="block" style="left:67px; top:54px; width:300px;">
    <p>Coaching &amp; Seminare für:</p>
    <ul class="bullets" style="margin-top:19px;">
      <li>hochsensible Menschen</li>
      <li>feinfühlige Kinder und Jugendliche</li>
      <li>private und berufliche Themen</li>
    </ul>
    <p style="margin-top:10px;">deutschlandweit online und in Präsenz</p>
  </section>

  <div class="photo photo--seminar-left" role="img" aria-label="Foto: Trainerin präsentiert am Flipchart im Seminarraum"></div>

  <section class="block" style="left:67px; top:499px; width:330px;">
    <p>Qualifikationen</p>
    <ul class="bullets">
      <li>Lehrerin für Sonderpädagogik</li>
      <li>Systemischer Coach</li>
      <li>Heilpraktikerin für Psychotherapie &amp; Fachberaterin Hochsensibilität</li>
      <li>Hypnose- und Atem-Coach</li>
      <li>Trainerin für Entspannung, Resilienz, Achtsamkeit, Stressmanagement, Schlafförderung</li>
      <li>Trainerin für das Kallwitzer Balance Ansatz (KBA®)</li>
    </ul>
    <p>u.a.</p>
  </section>

  <div class="photo photo--coaching" role="img" aria-label="Foto: Coach im Gespräch mit einem Klienten"></div>

  <section class="block" style="left:431px; top:335px; width:345px;">
    <p>Als Coach begleite ich Sie wertschätzend dabei, Ihre Wünsche zu realisieren, Ihre Ziele zu erreichen und Probleme zu lösen.</p>
    <p>Orientiert an Ihrem Anliegen entwickeln wir gemeinsam Wege, Ihre Ressourcen zu entdecken, Ihre Resilienz (psychische Widerstandskraft) zu stärken und Ihre sozialen Fähigkeiten (Skills) auszuschöpfen.</p>
    <p>Für die Erreichung Ihrer privaten oder beruflichen Ziele bekommen Sie ein individuell auf Sie zugeschnittenes lösungsorientiertes Coaching- und Beratungskonzept.</p>
    <p>Meine langjährige Erfahrung und professionellen Qualifikationen bieten Ihnen bewährt Qualität und Kompetenz.</p>
  </section>

  <div class="leaf-mark" role="img" aria-label="Blatt-Ornament"></div>

  <section class="block" style="left:820px; top:54px; width:355px;">
    <p>Lösungsorientiertes Coaching oder an Ihre Wünsche angepasste Inhouse-Seminare gestalte ich für Ihr Unternehmen und Ihr Mitarbeiter*innen-Team informativ, praxisnah und nachhaltig.</p>
    <p>Meine Themengebiete umfassen vielfältige Konzepte zur Nutzung von hochsensiblen Potentialen und Hochsensibilität im Berufsleben, zu Neurodiversität, Resilienz und Stärkung mentaler Gesundheit, zum Ressourcenorientierten Zielmanagement, zur Moderation von Intervision (Kollegiale Fallberatung), u.v.m.</p>
  </section>

  <div class="photo photo--seminar-right" role="img" aria-label="Foto: Trainerin leitet ein Seminar am Flipchart vor Teilnehmenden"></div>

  <section class="block" style="left:820px; top:612px; width:360px;">
    <p>Lernen Sie in krankenkassenzertifizierten Gesundheitskursen nach §20 SGB V eine wissenschaftlich anerkannte Entspannungstechnik, gelassenheit fördernde Achtsamkeitspraxis, nachhaltiges Stressmanagement oder&nbsp; stärkendes Resilienztraining nach dem bekannten Brevalo-Programm</p>
  </section>
</main>
</body>
</html>
```